Vorlan cards

I am in the auto motive, transportation business I would like a business card that is Something cool, modern edgy, having to do with car culture. I offer towing service for high and exotic cars. I also provide towing for collisions and car accidents. I offer open and enclosed transport nationwide.

Target Market(s)

Car culture people high end auto collectors

Industry/Entity Type

Towing car carrier

Contact Information for Business Card

My company colors black yellow and silver

Font styles to use
Serif

```html
<!DOCTYPE html>
<html lang="en">
<head>
<meta charset="utf-8">
<title>Vorlan Transportation business cards</title>
<link href="https://fonts.googleapis.com/css2?family=Montserrat:wght@400;500;700;800&display=swap" rel="stylesheet">
<style>
  :root {
    --ink: #0b0b0b;
    --paper: #ffffff;
    --yellow: #f7dc4a;
    --yellow-deep: #f3d21d;
    --stage: #e9e6e1;
    --muted: #f2f2f2;
  }
  * { box-sizing: border-box; margin: 0; padding: 0; }
  html, body { width: 900px; height: 1200px; overflow: hidden; }
  body {
    position: relative;
    background: var(--stage);
    font-family: "Montserrat", sans-serif;
    color: var(--ink);
  }
  .card {
    position: absolute;
    left: 80px;
    width: 742px;
    height: 444px;
    background: var(--paper);
    border-radius: 30px;
    overflow: hidden;
    box-shadow: 0 6px 18px rgba(0,0,0,.25);
  }
  .card--front { top: 132px; }
  .card--back { top: 638px; }

  .brand-mark {
    position: absolute;
    display: flex;
    align-items: center;
    gap: 12px;
    font-weight: 800;
    color: var(--ink);
    letter-spacing: 1px;
  }
  .brand-mark__dot {
    border-radius: 50%;
    background: var(--yellow-deep);
    flex: none;
  }
  .card--front .brand-mark { left: 42px; top: 100px; font-size: 46px; }
  .card--front .brand-mark__dot { width: 30px; height: 30px; }
  .card--back .brand-mark { left: 0; right: 0; top: 160px; justify-content: center; font-size: 72px; }
  .card--back .brand-mark__dot { width: 44px; height: 44px; }

  .name-tab {
    position: absolute;
    left: 0; top: 268px;
    width: 262px; height: 58px;
    background: var(--yellow);
    clip-path: polygon(0 0, 236px 0, 262px 58px, 0 58px);
    padding: 5px 0 0 28px;
  }
  .name-tab__name { font-size: 26px; font-weight: 700; line-height: 1.1; }
  .name-tab__role { font-size: 15px; font-weight: 500; line-height: 1.2; }

  .accent-stripe {
    position: absolute;
    left: 260px; top: 304px;
    width: 482px; height: 11px;
    background: var(--ink);
  }
  .info-band {
    position: absolute;
    left: 0; top: 326px;
    width: 742px; height: 118px;
    background: var(--ink);
    color: var(--paper);
  }
  .contact-list {
    position: absolute;
    left: 28px; top: 24px;
    list-style: none;
    font-size: 16px;
    line-height: 21px;
  }
  .contact-list li { display: flex; align-items: center; gap: 12px; }
  .contact-list svg { width: 13px; height: 13px; flex: none; }
  .address {
    position: absolute;
    left: 503px; top: 45px;
    padding-left: 20px;
    border-left: 2px solid var(--yellow-deep);
    font-size: 16px;
    line-height: 21px;
    font-style: normal;
  }

  .back-rule {
    position: absolute;
    left: 0; top: 365px;
    width: 742px; height: 5px;
    background: var(--yellow);
  }
  .back-band {
    position: absolute;
    left: 0; top: 382px;
    width: 742px; height: 62px;
    background: var(--ink);
    color: #e8e8e8;
    font-size: 16px;
    text-align: center;
    line-height: 52px;
  }
</style>
</head>
<body>
  <section class="card card--front" aria-label="Front of card">
    <div class="brand-mark"><span class="brand-mark__dot"></span>VORLAN</div>

    <div class="name-tab">
      <p class="name-tab__name">Daniel Reyes</p>
      <p class="name-tab__role">Owner</p>
    </div>
    <div class="accent-stripe"></div>

    <div class="info-band">
      <ul class="contact-list">
        <li>
          <svg viewBox="0 0 16 16" aria-hidden="true"><path fill="var(--yellow-deep)" d="M3 1h3l1.5 4-2 1.3a9 9 0 0 0 4.2 4.2L11 8.5l4 1.5v3a2 2 0 0 1-2 2A12 12 0 0 1 1 3a2 2 0 0 1 2-2z"/></svg>
          (555) 014-2280
        </li>
        <li>
          <svg viewBox="0 0 16 16" aria-hidden="true"><rect x="1" y="3" width="14" height="10" fill="var(--yellow-deep)"/><path d="M1 3l7 6 7-6" fill="none" stroke="var(--ink)" stroke-width="1.4"/></svg>
          info@vorlantransportation.com
        </li>
        <li>
          <svg viewBox="0 0 16 16" aria-hidden="true"><circle cx="8" cy="8" r="7" fill="var(--yellow-deep)"/><path d="M1 8h14M8 1c-3 4-3 10 0 14M8 1c3 4 3 10 0 14" fill="none" stroke="var(--ink)" stroke-width="1.1"/></svg>
          www.vorlantransportation.com
        </li>
      </ul>
      <address class="address">48 Harlow Street<br>Fenwick, PA 17000</address>
    </div>
  </section>

  <section class="card card--back" aria-label="Back of card">
    <div class="brand-mark"><span class="brand-mark__dot"></span>VORLAN</div>
    <div class="back-rule"></div>
    <div class="back-band">www.vorlantransportation</div>
  </section>
</body>
</html>
```